Poster for Office

Looking for an edgy, beautiful poster to hang up in my office that uses the quotes located below and potentially the image attached.

Title: Hadley's Maxims

Must have the following quotes included (punctuation and capitalization are flexible, do what you think looks the best they also don't need the quotation symbols):

"Don't order fish at a steakhouse"
"Be bold. The more you tell, the more you sell"
"admit nothing, deny everything, launch counterattack."
"avoid obviousness"
"never do anything until you're ready to do it"
"look good=feel good"
"always keep the advantage"
"never complain, never explain"
"Lay low, play dumb, keep moving"

Quotes

• Title: Hadley's Maxims

"avoid obviousness"
"look good=feel good"

```html
<!DOCTYPE html>
<html lang="en">
<head>
<meta charset="utf-8">
<title>Hadley's Maxims</title>
<link rel="stylesheet" href="https://fonts.googleapis.com/css2?family=Josefin+Sans:wght@100;200;700&display=swap">
<style>
  :root {
    --ink: #ffffff;
    --ink-soft: rgba(255, 255, 255, 0.92);
    --sky: #a9b8dc;
    --steel: #8a94ab;
    --royal: #2f4fb8;
    --cobalt: #1c2f9a;
    --navy: #0e1640;
    --night: #050608;
  }
  html, body {
    margin: 0;
    padding: 0;
    overflow: hidden;
    background: var(--night);
  }
  .poster {
    position: relative;
    width: 843px;
    height: 1200px;
    overflow: hidden;
    font-family: "Josefin Sans", "Century Gothic", sans-serif;
    color: var(--ink);
    text-transform: uppercase;
  }
  .backdrop {
    position: absolute;
    inset: 0;
    background:
      radial-gradient(ellipse 260px 420px at 300px 420px, rgba(20, 30, 90, 0.55), transparent 70%),
      linear-gradient(135deg, var(--sky) 0%, var(--steel) 20%, var(--royal) 42%, var(--cobalt) 58%, var(--navy) 78%, var(--night) 100%);
  }
  .line {
    position: absolute;
    margin: 0;
    line-height: 1;
    white-space: nowrap;
  }
  .thin { font-weight: 100; color: var(--ink-soft); }
  .bold { font-weight: 700; }

  .steak-1     { left: 0;    top: 2px;   font-size: 60px; letter-spacing: 6px; }
  .steak-2     { left: 0;    top: 64px;  font-size: 60px; letter-spacing: 5px; }
  .be-bold     { left: 552px; top: 64px; font-size: 58px; letter-spacing: 1px; }
  .tell        { left: 108px; top: 128px; font-size: 63px; letter-spacing: 0; }
  .sell        { left: 108px; top: 191px; font-size: 63px; letter-spacing: 0; }
  .admit       { left: 0; top: 262px; font-size: 60px; letter-spacing: 4px; }
  .deny        { left: 0; top: 323px; font-size: 60px; letter-spacing: 3px; }
  .launch      { left: 0; top: 383px; font-size: 60px; letter-spacing: 3px; }
  .counter     { left: 0; top: 444px; font-size: 60px; letter-spacing: 3px; }
  .ready-1     { left: 0; top: 505px; font-size: 54px; letter-spacing: 0; }
  .ready-2     { left: 0; top: 561px; font-size: 54px; letter-spacing: 0; }
  .keep-1      { right: 8px; top: 616px; font-size: 60px; letter-spacing: 4px; }
  .keep-2      { right: 6px; top: 676px; font-size: 60px; letter-spacing: 5px; }
  .obvious     { left: 0; top: 741px; font-size: 37px; letter-spacing: 1px; }
  .complain-1  { left: 0; top: 784px; font-size: 58px; letter-spacing: 0; }
  .complain-2  { left: 0; top: 840px; font-size: 58px; letter-spacing: 0; }
  .look-good   { left: 0; top: 903px; font-size: 56px; letter-spacing: 1px; }
  .lay-low-1   { left: 0; top: 966px; font-size: 50px; letter-spacing: 1px; }
  .lay-low-2   { left: 0; top: 1018px; font-size: 50px; letter-spacing: 1px; }

  .title {
    position: absolute;
    right: 2px;
    bottom: 4px;
    margin: 0;
    text-align: right;
    font-weight: 700;
    line-height: 0.95;
  }
  .title-top    { display: block; font-size: 86px; }
  .title-bottom { display: block; font-size: 86px; }
</style>
</head>
<body>
  <main class="poster">
    <div class="backdrop" role="img" aria-label="Portrait photograph of a man in a suit, tinted blue, over a textured pattern of blue, grey and black diagonal stripes"></div>

    <p class="line thin steak-1">Don’t order fish at</p>
    <p class="line thin steak-2">a steakhouse</p>
    <p class="line bold be-bold">Be bold</p>
    <p class="line bold tell">The more you tell</p>
    <p class="line bold sell">The more you sell</p>

    <p class="line thin admit">Admit nothing,</p>
    <p class="line thin deny">Deny everything,</p>
    <p class="line thin launch">Launch</p>
    <p class="line thin counter">Counterattack.</p>

    <p class="line bold ready-1">Never do anything until</p>
    <p class="line bold ready-2">You’re ready to do it.</p>

    <p class="line thin keep-1">Always keep</p>
    <p class="line thin keep-2">the advantage.</p>

    <p class="line thin obvious">Avoid obviousness.</p>

    <p class="line bold complain-1">Never complain,</p>
    <p class="line bold complain-2">Never explain.</p>

    <p class="line thin look-good">Look good = feel good.</p>

    <p class="line thin lay-low-1">Lay low, play dumb,</p>
    <p class="line thin lay-low-2">Keep moving.</p>

    <h1 class="title">
      <span class="title-top">Hadley’s</span>
      <span class="title-bottom">Maxims</span>
    </h1>
  </main>
</body>
</html>
```